QRTvBridgeline Wellroute Mobile Experience

Design the following Observation and Well Route mobile app pages so they are very modern, cool and engaging.
We would also like to modernize our current splash experience (attached).

Observation and Well Route wireframes:
https://kz4pwn.protoview.example/#g=1&p=observations__-_categories

DO NOT SUBMIT LOGO REDESIGNS. Submit all screens for the above wireframes. If you can improve the Splash screen this is a bonus. Use the same color scheme and logo.

Competitive sample:
https://apps.storefrontdemo.example/details?id=com.tendrix.iphone

```html
<!DOCTYPE html>
<html lang="en">
<head>
<meta charset="utf-8">
<title>Submit Observation</title>
<link href="https://fonts.googleapis.com/css2?family=Lato:wght@400;700&display=swap" rel="stylesheet">
<style>
  :root {
    --orange: #f8a11e;
    --orange-mid: #e8a53a;
    --teal: #6bb4cf;
    --white: #ffffff;
    --ink: #3b3b3b;
    --tab-muted: #b9b9b9;
    --band: #fdeeed;
    --divider: #ececec;
    --chevron: #5aa9c9;
    --icon-fill: #f08a7a;
  }
  * { margin: 0; padding: 0; box-sizing: border-box; }
  html, body { width: 675px; height: 1200px; overflow: hidden; }
  body {
    position: relative;
    font-family: "Lato", sans-serif;
    background: linear-gradient(180deg, var(--orange) 0%, var(--orange-mid) 25%, var(--teal) 62%, var(--teal) 100%);
  }
  .app-bar { position: absolute; top: 0; left: 0; width: 675px; height: 118px; }
  .app-bar__back { position: absolute; left: 38px; top: 44px; }
  .app-bar__title {
    position: absolute; left: 0; width: 675px; top: 41px;
    text-align: center; color: var(--white); font-size: 25px; font-weight: 400; letter-spacing: .2px;
  }
  .app-bar__action { position: absolute; top: 39px; }
  .app-bar__action--help { left: 551px; }
  .app-bar__action--add { left: 615px; }

  .sheet {
    position: absolute; left: 20px; top: 126px; width: 635px; height: 1053px;
    background: var(--white); border-radius: 14px; overflow: hidden;
  }
  .tabs {
    position: absolute; top: 42px; left: 27px; height: 68px;
    display: flex; gap: 38px; white-space: nowrap;
  }
  .tabs__item {
    position: relative; font-size: 23px; font-weight: 700;
    letter-spacing: 1.1px; color: var(--tab-muted); line-height: 1.2;
  }
  .tabs__item--active { color: var(--orange); }
  .tabs__item--active::after {
    content: ""; position: absolute; left: 50%; top: 45px; width: 85px; height: 5px;
    margin-left: -42px; border-radius: 3px; background: var(--orange);
  }

  .category {
    position: absolute; top: 110px; left: 0; width: 100%; height: 110px;
    background: var(--band); display: flex; align-items: center;
  }
  .category__icon {
    margin-left: 37px; width: 42px; height: 38px; border-radius: 8px;
    background: var(--icon-fill);
  }
  .category__name { margin-left: 16px; font-size: 26px; font-weight: 400; color: var(--ink); }

  .options { position: absolute; top: 220px; left: 25px; width: 585px; list-style: none; }
  .options__item {
    position: relative; height: 88px; border-bottom: 1.5px solid var(--divider);
    display: flex; align-items: center; font-size: 21.5px; color: var(--ink); white-space: nowrap;
  }
  .options__item:first-child { height: 86px; }
  .options__item:last-child { border-bottom: none; }
  .options__chevron { position: absolute; right: -6px; top: 50%; margin-top: -8px; }
</style>
</head>
<body>
  <header class="app-bar">
    <svg class="app-bar__back" width="24" height="30" viewBox="0 0 24 30" aria-label="Back">
      <path d="M17 3 L6 15 L17 27" fill="none" stroke="#fff" stroke-width="3" stroke-linecap="round" stroke-linejoin="round"/>
    </svg>
    <h1 class="app-bar__title">Submit Observation</h1>
    <svg class="app-bar__action app-bar__action--help" width="42" height="42" viewBox="0 0 42 42" aria-label="Help">
      <circle cx="21" cy="21" r="19" fill="none" stroke="#fff" stroke-width="2.5"/>
      <path d="M15.5 16.5a5.5 5.5 0 1 1 8 4.9c-1.6.9-2.5 1.9-2.5 3.6v1" fill="none" stroke="#fff" stroke-width="2.5" stroke-linecap="round"/>
      <circle cx="21" cy="31" r="1.7" fill="#fff"/>
    </svg>
    <svg class="app-bar__action app-bar__action--add" width="42" height="42" viewBox="0 0 42 42" aria-label="Add">
      <circle cx="21" cy="21" r="19" fill="none" stroke="#fff" stroke-width="2.5"/>
      <path d="M21 12v18M12 21h18" stroke="#fff" stroke-width="2.5" stroke-linecap="round"/>
    </svg>
  </header>

  <main class="sheet">
    <nav class="tabs">
      <span class="tabs__item">CARE PLAN</span>
      <span class="tabs__item">WELL ROUTE</span>
      <span class="tabs__item tabs__item--active">OBSERVATIONS</span>
      <span class="tabs__item">NOTES</span>
    </nav>

    <section class="category">
      <div class="category__icon" role="img" aria-label="Medication category icon"></div>
      <h2 class="category__name">Medication</h2>
    </section>

    <ul class="options">
      <li class="options__item">Patient does not have all their medication(s)
        <svg class="options__chevron" width="11" height="16" viewBox="0 0 11 16"><path d="M2 2l6 6-6 6" fill="none" stroke="var(--chevron)" stroke-width="2.6" stroke-linecap="round" stroke-linejoin="round"/></svg></li>
      <li class="options__item">Patient is refusing to take medication(s)
        <svg class="options__chevron" width="11" height="16" viewBox="0 0 11 16"><path d="M2 2l6 6-6 6" fill="none" stroke="var(--chevron)" stroke-width="2.6" stroke-linecap="round" stroke-linejoin="round"/></svg></li>
      <li class="options__item">Patient has forgotten to take 1 or more medication(s)
        <svg class="options__chevron" width="11" height="16" viewBox="0 0 11 16"><path d="M2 2l6 6-6 6" fill="none" stroke="var(--chevron)" stroke-width="2.6" stroke-linecap="round" stroke-linejoin="round"/></svg></li>
      <li class="options__item">Patient has over-consumed medication(s)
        <svg class="options__chevron" width="11" height="16" viewBox="0 0 11 16"><path d="M2 2l6 6-6 6" fill="none" stroke="var(--chevron)" stroke-width="2.6" stroke-linecap="round" stroke-linejoin="round"/></svg></li>
      <li class="options__item">Other
        <svg class="options__chevron" width="11" height="16" viewBox="0 0 11 16"><path d="M2 2l6 6-6 6" fill="none" stroke="var(--chevron)" stroke-width="2.6" stroke-linecap="round" stroke-linejoin="round"/></svg></li>
    </ul>
  </main>
</body>
</html>
```